Top 100

I have attached a sheet with the information that we would like on a 2'by 3' poster. If you can take this info and make it look more appealing, that is what we are looking for.

I have also attached our high res logo. We just pulled the KVRT and Trelvex logos off the web

```html
<!DOCTYPE html>
<html lang="en">
<head>
<meta charset="utf-8">
<title>Corvane Advisors – Top 100 Poster</title>
<link href="https://fonts.googleapis.com/css2?family=Roboto+Condensed:wght@300;400;700&display=swap" rel="stylesheet">
<style>
  :root {
    --navy: #163a63;
    --orange: #f7941d;
    --white: #ffffff;
    --slate: #34506e;
    --page: #ffffff;
  }
  * { margin: 0; padding: 0; box-sizing: border-box; }
  html, body { width: 1200px; height: 1000px; overflow: hidden; background: var(--page); }
  body { position: relative; font-family: "Roboto Condensed", "Arial Narrow", sans-serif; }

  .poster { position: absolute; left: 283px; top: 30px; width: 627px; height: 938px; background: var(--navy); }

  .poster-header {
    position: absolute; left: 0; top: 0; width: 627px; height: 158px;
    background: var(--white);
    display: flex; align-items: center; justify-content: center;
  }
  .brand-name { color: var(--slate); font-weight: 700; font-size: 50px; letter-spacing: 0.5px; }

  .photo-band { position: absolute; left: 0; top: 158px; width: 627px; height: 117px; display: flex; }
  .photo-columns { width: 375px; height: 100%; background: linear-gradient(90deg, #4a4d52 0%, #9a9ea3 30%, #6d7075 55%, #b4b7ba 80%, #7d8085 100%); }
  .photo-glass { flex: 1; height: 100%; background: linear-gradient(135deg, #d7e9f5 0%, #7fb2d8 45%, #b9d8ee 75%, #e6f1f9 100%); }

  .accent-top { position: absolute; left: 0; top: 275px; width: 627px; height: 30px; background: var(--orange); }
  .accent-bottom { position: absolute; left: 0; top: 918px; width: 627px; height: 20px; background: var(--orange); }

  .highlight {
    position: absolute; left: 35px; width: 402px; height: 169px;
    border: 2px solid var(--white);
    display: flex; flex-direction: column; align-items: center; justify-content: center;
    text-align: center; color: var(--white);
  }
  .highlight-lead { font-weight: 300; font-size: 21px; line-height: 1.2; }
  .highlight-title { color: var(--orange); font-weight: 700; font-size: 33px; line-height: 1.2; }
  .highlight-note { font-weight: 300; font-size: 21px; line-height: 1.25; }

  .connector { position: absolute; left: 437px; width: 26px; height: 2px; background: var(--white); }

  .partner-tile {
    position: absolute; left: 463px; width: 136px; height: 136px; background: var(--white);
    display: flex; align-items: center; justify-content: center;
  }
  .partner-name { font-weight: 700; font-size: 22px; color: var(--navy); }
  .partner-name.is-brand { color: var(--slate); font-size: 18px; }
</style>
</head>
<body>
  <main class="poster">
    <header class="poster-header">
      <span class="brand-name">Corvane Advisors</span>
    </header>

    <div class="photo-band">
      <div class="photo-columns" role="img" aria-label="Photo of classical stone columns on a financial building"></div>
      <div class="photo-glass" role="img" aria-label="Photo of a modern glass skyscraper looking upward"></div>
    </div>
    <div class="accent-top"></div>

    <section class="highlight" style="top:334px;">
      <p class="highlight-title">2015 - Top 100<br>Wealth Management Firm</p>
      <p class="highlight-note">Only Greater Cincinnati Firm Selected</p>
    </section>
    <div class="connector" style="top:417px;"></div>
    <div class="partner-tile" style="top:350px;"><span class="partner-name">KVRT</span></div>

    <section class="highlight" style="top:523px;">
      <p class="highlight-lead">In 2015 Launches the</p>
      <p class="highlight-title">Nation’s Only Actively<br>ManagedSmall Cap ETF</p>
      <p class="highlight-note">(CSCX: TRELVEX)</p>
    </section>
    <div class="connector" style="top:607px;"></div>
    <div class="partner-tile" style="top:540px;"><span class="partner-name">Trelvex</span></div>

    <section class="highlight" style="top:712px;">
      <p class="highlight-lead">Nationally Recognised Advisor</p>
      <p class="highlight-title">Providing Boutique Wealth<br>Management Since 1999</p>
    </section>
    <div class="connector" style="top:796px;"></div>
    <div class="partner-tile" style="top:729px;"><span class="partner-name is-brand">Corvane</span></div>

    <div class="accent-bottom"></div>
  </main>
</body>
</html>
```